Childcare Centre Franchise Website Design

Our business is Childcare centre, and we are the franchise with 4 centres currently, we would like to have the website similar as the link below,
https://www.brambleoak.edu.au/
with the same items, functions and pages. Locations information for all centres, and have pages for each centre. Additionally, we will need a page for online enrolment.
Our logo is attached.

```html
<!DOCTYPE html>
<html lang="en">
<head>
<meta charset="utf-8">
<title>Little Meadow Childcare</title>
<link href="https://fonts.googleapis.com/css2?family=Lexend:wght@400;500;600;700&family=Lato:wght@300;400;700&display=swap" rel="stylesheet">
<style>
:root{
  --teal:#2fa9a4;
  --teal-dark:#23948f;
  --teal-soft:#d7efee;
  --brown:#7b3a2c;
  --ink:#1f1f1f;
  --body:#3a3a3a;
  --white:#ffffff;
}
*{box-sizing:border-box;margin:0;padding:0}
html,body{width:1200px;height:3795px;overflow:hidden;background:var(--white)}
body{font-family:"Lato",sans-serif;color:var(--body)}
.page{position:relative;width:1200px;height:3795px;overflow:hidden}
.abs{position:absolute}

/* header */
.brand{left:97px;top:26px;width:140px;text-align:center}
.brand-dot{width:46px;height:46px;border-radius:50%;background:var(--teal);margin:0 auto 6px}
.brand-name{font-family:"Lexend",sans-serif;font-weight:600;font-size:14px;color:var(--brown);letter-spacing:.5px}
.site-search{left:312px;top:24px;width:406px;height:42px;border:1.5px solid #555;border-radius:21px;padding:0 20px;display:flex;align-items:center;justify-content:space-between;font-size:16px;color:#999}
.phone{left:740px;top:34px;font-size:17px;color:var(--ink);display:flex;align-items:center;gap:8px}
.find-btn{left:932px;top:26px;width:156px;height:42px;border-radius:21px;background:var(--teal);color:#fff;font-size:15px;display:flex;align-items:center;justify-content:center;gap:8px}
.nav{left:313px;top:81px;width:780px;display:flex;justify-content:space-between;font-size:15px;color:var(--ink)}

/* hero */
.hero{left:0;top:128px;width:1200px;height:640px;background:linear-gradient(180deg,#5fa5a6 0%,#4f95a0 50%,#3d7f8c 100%)}
.hero-title{left:0;top:312px;width:1200px;text-align:center;color:#fff;font-family:"Lexend",sans-serif;line-height:1.1}
.hero-title .small{font-size:36px;font-weight:500;display:block}
.hero-title .big{font-size:46px;font-weight:500;display:block}
.enrol-card{left:293px;top:475px;width:615px;height:187px;background:#fff;border-radius:22px;text-align:center}
.enrol-card h2{font-family:"Lexend",sans-serif;font-weight:500;font-size:28px;color:var(--ink);margin-top:33px}
.postcode{position:absolute;left:38px;top:95px;width:540px;height:50px;border:1.5px solid #444;border-radius:6px;display:flex;align-items:center;padding-left:26px;font-size:17px;color:var(--ink)}
.postcode .btn{position:absolute;right:7px;top:6px;width:114px;height:36px}

/* buttons */
.btn{background:var(--brown);color:#fff;border-radius:6px;display:flex;align-items:center;justify-content:center;font-size:16px;font-family:"Lato",sans-serif}

/* sections */
.section-title{left:0;width:1200px;text-align:center;font-family:"Lexend",sans-serif;font-weight:700;font-size:27px;color:var(--teal);line-height:41px;letter-spacing:.3px}

.support-card{top:992px;width:305px;height:340px;border:1.5px solid var(--teal);border-radius:20px;text-align:center}
.support-card h3{font-family:"Lexend",sans-serif;font-weight:400;font-size:21px;color:var(--ink);line-height:30px;margin-top:33px}
.support-card p{font-size:17px;line-height:30px;color:var(--body);font-weight:300;margin:30px 22px 0}
.support-card .btn{position:absolute;left:50%;transform:translateX(-50%);bottom:31px;width:115px;height:38px}

.approach-img{top:1591px;width:204px;height:199px;border-radius:20px}
.approach-label{top:1824px;width:260px;text-align:center;font-family:"Lexend",sans-serif;font-size:21px;line-height:29px;color:var(--ink);letter-spacing:.8px}

.news-card{top:2218px;width:310px;height:395px;border-radius:20px;background:#fff;box-shadow:0 0 10px rgba(0,0,0,.12)}
.news-card .photo{position:absolute;left:13px;top:17px;width:284px;height:144px;border-radius:14px}
.news-card h4{position:absolute;left:21px;top:182px;font-family:"Lexend",sans-serif;font-weight:700;font-size:15px;color:var(--teal);letter-spacing:.6px}
.news-card p{position:absolute;left:21px;top:217px;width:272px;font-size:18px;line-height:26px;color:var(--body);font-weight:300}
.news-card .btn{position:absolute;left:19px;top:332px;width:146px;height:41px;font-size:17px}

.state{top:2862px;width:300px;text-align:center;font-family:"Lexend",sans-serif;font-weight:700;font-size:17px;color:var(--ink);letter-spacing:.6px}
.centre{width:330px;height:98px;display:flex;gap:18px}
.centre .thumb{width:104px;height:98px;border-radius:14px;flex:none}
.centre h5{font-family:"Lexend",sans-serif;font-weight:700;font-size:14px;color:var(--ink);letter-spacing:.8px;margin-top:12px}
.centre p{font-size:15px;line-height:25px;color:var(--body);font-weight:300;margin-top:12px}
.arrow{width:46px;height:46px;border-radius:50%;background:#fff;box-shadow:0 0 8px rgba(0,0,0,.2);display:flex;align-items:center;justify-content:center}

/* footer */
.footer-bg{left:0;top:3370px;width:1200px;height:425px}
.footer-brand{left:108px;top:3518px;width:155px;text-align:center;color:#fff}
.footer-brand .brand-dot{background:#fff;width:50px;height:50px}
.footer-brand .brand-name{color:#fff;font-size:15px}
.social{top:3627px;width:32px;height:32px;border-radius:50%}
.foot-col{top:3518px;color:#fff;font-size:15px;line-height:26px;font-weight:300}
.foot-col h6{font-family:"Lato",sans-serif;font-weight:700;font-size:15px;margin-bottom:1px}
.foot-rule{left:0;top:3738px;width:1200px;height:1px;background:rgba(255,255,255,.5)}
.copyright{left:0;top:3754px;width:1200px;text-align:center;color:#fff;font-size:15px;font-weight:300}
</style>
</head>
<body>
<div class="page">

  <!-- header -->
  <div class="abs brand"><div class="brand-dot"></div><div class="brand-name">LITTLE MEADOW</div></div>
  <div class="abs site-search"><span>Search</span>
    <svg width="16" height="16" viewBox="0 0 16 16"><circle cx="6.5" cy="6.5" r="5" fill="none" stroke="#777" stroke-width="1.6"/><line x1="10.3" y1="10.3" x2="15" y2="15" stroke="#777" stroke-width="1.6"/></svg>
  </div>
  <div class="abs phone">
    <svg width="15" height="15" viewBox="0 0 24 24"><path fill="#2fa9a4" d="M6.6 10.8a15.5 15.5 0 0 0 6.6 6.6l2.2-2.2c.3-.3.7-.4 1-.2 1.1.4 2.3.6 3.6.6.6 0 1 .4 1 1V20c0 .6-.4 1-1 1A17 17 0 0 1 3 4c0-.6.4-1 1-1h3.5c.6 0 1 .4 1 1 0 1.3.2 2.5.6 3.6.1.3 0 .7-.2 1z"/></svg>
    +1 888 888 8888
  </div>
  <div class="abs find-btn">
    <svg width="13" height="17" viewBox="0 0 12 16"><path fill="#fff" d="M6 0a6 6 0 0 0-6 6c0 4.5 6 10 6 10s6-5.5 6-10a6 6 0 0 0-6-6zm0 8.2A2.2 2.2 0 1 1 6 3.8a2.2 2.2 0 0 1 0 4.4z"/></svg>
    Find A Centre
  </div>
  <nav class="abs nav">
    <span>Childcare &amp; Education</span><span>Childcare Centres</span><span>Childcare Subsidy</span><span>News &amp; Advice</span><span>Careers</span><span>About Us</span>
  </nav>

  <!-- hero -->
  <div class="abs hero" role="img" aria-label="Photo of smiling school children standing together"></div>
  <svg class="abs" style="left:0;top:670px" width="1200" height="120" viewBox="0 0 1200 120">
    <path d="M0 60 C150 20 250 100 420 70 C560 45 640 95 800 60 C950 25 1050 80 1200 55 L1200 120 L0 120Z" fill="#cfeceb" opacity=".8"/>
    <path d="M0 85 C180 50 300 110 480 85 C620 65 720 110 880 85 C1020 62 1100 95 1200 80 L1200 120 L0 120Z" fill="#fff"/>
  </svg>
  <div class="abs hero-title"><span class="small">Welcome to</span><span class="big">Little Meadow</span></div>
  <div class="abs enrol-card">
    <h2>FIND YOUR CENTRE TO ENROL</h2>
    <div class="postcode">Enter Postcode<div class="btn">Search</div></div>
  </div>

  <!-- support -->
  <h2 class="abs section-title" style="top:848px">WE’RE HERE TO SUPPORT THE<br>WHOLE FAMILY</h2>
  <div class="abs support-card" style="left:105px"><h3>CHILD CARE<br>SUBSIDY</h3><p>Lorem ipsum dolor sit amet, consectetur adipiscing elit, sed do eiusmod tempor incididunt ut labore et aliqua.</p><div class="btn">Learn More</div></div>
  <div class="abs support-card" style="left:443px"><h3>WHY<br>LITTLE MEADOW?</h3><p>Lorem ipsum dolor sit amet, consectetur adipiscing elit, sed do eiusmod tempor incididunt ut labore et aliqua.</p><div class="btn">Learn More</div></div>
  <div class="abs support-card" style="left:797px"><h3>HEALTH &amp;<br>WELLBEING</h3><p>Lorem ipsum dolor sit amet, consectetur adipiscing elit, sed do eiusmod tempor incididunt ut labore et aliqua.</p><div class="btn">Learn More</div></div>

  <!-- approach -->
  <h2 class="abs section-title" style="top:1448px">A LOVE OF LEARNING. CONFIDENCE. CURIOSITY.<br>HERE ARE SOME OF THE WAYS WE HELP CHILDREN THRIVE.</h2>
  <div class="abs approach-img" style="left:106px;background:linear-gradient(135deg,#d9c39a,#3c5f9c)" role="img" aria-label="Photo of children writing at a classroom desk"></div>
  <div class="abs approach-img" style="left:378px;background:linear-gradient(180deg,#7fb3d9,#8a9aa3 60%,#6f8f4f)" role="img" aria-label="Photo of a modern school building"></div>
  <div class="abs approach-img" style="left:639px;background:linear-gradient(135deg,#e6ddd3,#b0714a)" role="img" aria-label="Photo of a child holding carrot slices"></div>
  <div class="abs approach-img" style="left:895px;background:linear-gradient(135deg,#e9e4dc,#b5614a)" role="img" aria-label="Photo of children raising their arms"></div>
  <div class="abs approach-label" style="left:78px">HIGH-QUALITY<br>CURRICULUM</div>
  <div class="abs approach-label" style="left:350px">EXICITING<br>ENVIRONMENTS</div>
  <div class="abs approach-label" style="left:618px">WELLBEING &amp;<br>NUTRITION</div>
  <div class="abs approach-label" style="left:875px">COMMUNITY<br>CONNECTIONS</div>
  <div class="abs btn" style="left:496px;top:1952px;width:224px;height:38px;font-size:17px">Discover Our Approach</div>

  <!-- news -->
  <h2 class="abs section-title" style="top:2085px">LATEST NEWS &amp; ADVICE FROM OUR<br>TEAM OF EXPERTS</h2>
  <article class="abs news-card" style="left:96px"><div class="photo" style="background:linear-gradient(180deg,#b9c6c9,#8e8f97)" role="img" aria-label="Photo of children running down a school hallway"></div><h4>LOREM IPSUM DOLOR SIT</h4><p>Lorem ipsum dolor sit amet, consectetur adipiscing elit, sed do eiusmod tempor incididunt ut labore et dolore magna aliqua.</p><div class="btn">Read More</div></article>
  <article class="abs news-card" style="left:445px"><div class="photo" style="background:linear-gradient(135deg,#c9b7a2,#3d4e72)" role="img" aria-label="Photo of a teacher helping students at a table"></div><h4>LOREM IPSUM DOLOR SIT</h4><p>Lorem ipsum dolor sit amet, consectetur adipiscing elit, sed do eiusmod tempor incididunt ut labore et dolore magna aliqua.</p><div class="btn">Read More</div></article>
  <article class="abs news-card" style="left:793px"><div class="photo" style="background:linear-gradient(135deg,#8fb0cf,#d09a76)" role="img" aria-label="Photo of three smiling children sitting together"></div><h4>LOREM IPSUM DOLOR SIT</h4><p>Lorem ipsum dolor sit amet, consectetur adipiscing elit, sed do eiusmod tempor incididunt ut labore et dolore magna aliqua.</p><div class="btn">Read More</div></article>

  <!-- centres -->
  <h2 class="abs section-title" style="top:2709px">FIND YOUR VILLAGE<br>CHILDCARE CENTRES BY STATE</h2>
  <div class="abs state" style="left:59px">VICTORIA</div>
  <div class="abs state" style="left:442px">NEW SOUTH WALES</div>
  <div class="abs state" style="left:804px">QUEENSLAND</div>

  <div class="abs centre" style="left:115px;top:2947px"><div class="thumb" style="background:linear-gradient(135deg,#d8c9b4,#9a6f55)" role="img" aria-label="Photo of a classroom"></div><div><h5>LOREM IPSUM</h5><p>Lorem ipsum dolor sit<br>amet, adipiscing elit.</p></div></div>
  <div class="abs centre" style="left:115px;top:3066px"><div class="thumb" style="background:linear-gradient(135deg,#d6c19a,#3c5f9c)" role="img" aria-label="Photo of children studying"></div><div><h5>LOREM IPSUM</h5><p>Lorem ipsum dolor sit<br>amet, adipiscing elit.</p></div></div>
  <div class="abs centre" style="left:115px;top:3182px"><div class="thumb" style="background:linear-gradient(135deg,#cbd6c4,#a26a55)" role="img" aria-label="Photo of a classroom lesson"></div><div><h5>LOREM IPSUM</h5><p>Lorem ipsum dolor sit<br>amet, adipiscing elit.</p></div></div>

  <div class="abs centre" style="left:462px;top:2947px"><div class="thumb" style="background:linear-gradient(180deg,#b9c6c9,#8e8f97)" role="img" aria-label="Photo of children in a hallway"></div><div><h5>LOREM IPSUM</h5><p>Lorem ipsum dolor sit<br>amet, adipiscing elit.</p></div></div>
  <div class="abs centre" style="left:462px;top:3066px"><div class="thumb" style="background:linear-gradient(135deg,#c9b7a2,#3d4e72)" role="img" aria-label="Photo of a teacher with students"></div><div><h5>LOREM IPSUM</h5><p>Lorem ipsum dolor sit<br>amet, adipiscing elit.</p></div></div>
  <div class="abs centre" style="left:462px;top:3182px"><div class="thumb" style="background:linear-gradient(135deg,#e6dccd,#b9876a)" role="img" aria-label="Photo of students raising hands"></div><div><h5>LOREM IPSUM</h5><p>Lorem ipsum dolor sit<br>amet, adipiscing elit.</p></div></div>

  <div class="abs centre" style="left:810px;top:2947px"><div class="thumb" style="background:linear-gradient(135deg,#7fa6c7,#d9a56a)" role="img" aria-label="Photo of children smiling"></div><div><h5>LOREM IPSUM</h5><p>Lorem ipsum dolor sit<br>amet, adipiscing elit.</p></div></div>
  <div class="abs centre" style="left:810px;top:3066px"><div class="thumb" style="background:linear-gradient(135deg,#6f8a7e,#c7a47e)" role="img" aria-label="Photo of a classroom with desks"></div><div><h5>LOREM IPSUM</h5><p>Lorem ipsum dolor sit<br>amet, adipiscing elit.</p></div></div>
  <div class="abs centre" style="left:810px;top:3182px"><div class="thumb" style="background:linear-gradient(135deg,#9fb4c8,#c98f6b)" role="img" aria-label="Photo of children reading together"></div><div><h5>LOREM IPSUM</h5><p>Lorem ipsum dolor sit<br>amet, adipiscing elit.</p></div></div>

  <div class="abs arrow" style="left:30px;top:3081px"><svg width="12" height="18" viewBox="0 0 12 18"><path d="M9 2 3 9l6 7" fill="none" stroke="#111" stroke-width="2.5"/></svg></div>
  <div class="abs arrow" style="left:1118px;top:3081px"><svg width="12" height="18" viewBox="0 0 12 18"><path d="M3 2l6 7-6 7" fill="none" stroke="#111" stroke-width="2.5"/></svg></div>

  <!-- footer -->
  <svg class="abs footer-bg" viewBox="0 0 1200 425" preserveAspectRatio="none">
    <path d="M0 50 C120 10 200 60 320 30 C460 -5 560 70 700 40 C840 10 950 50 1060 20 C1120 5 1170 15 1200 25 L1200 425 L0 425Z" fill="#cfeceb"/>
    <path d="M0 95 C140 60 250 120 420 80 C560 48 660 115 820 85 C960 58 1060 100 1200 70 L1200 425 L0 425Z" fill="#2fa9a4"/>
  </svg>
  <div class="abs footer-brand"><div class="brand-dot"></div><div class="brand-name">LITTLE MEADOW</div></div>
  <div class="abs social" style="left:114px;background:#1da1f2"></div>
  <div class="abs social" style="left:159px;background:#3b5998"></div>
  <div class="abs social" style="left:208px;background:#d6249f"></div>

  <div class="abs foot-col" style="left:374px"><h6>Find Your Closest Centre</h6>Victoria<br>New South Wales<br>Queensland<br>South Australia<br>Australian Capital Territory<br>Victoria</div>
  <div class="abs foot-col" style="left:665px"><h6>Quick Links</h6>Childcare &amp; Education<br>Childcare Centres<br>Childcare Subsidy<br>News &amp; Advice<br>Careers<br>About Us</div>
  <div class="abs foot-col" style="left:927px"><h6>Help Links</h6>Support<br>Terms &amp; Conditions<br>FAQ<br>Privacy Policy</div>
  <div class="abs foot-rule"></div>
  <div class="abs copyright">© Copyrights 2023 Little Meadow Childcare | All Rights Reserved</div>
</div>
</body>
</html>
```